Australian IT Company New Logo Business Cards Required

We are a computer consultancy / MSP located in Brisbane Australia looking to have business cards designed with our new logo, we are looking for something professional that catches the eye.
I can provide the logo in other formats if required, let's see what you can create!

```html
<!DOCTYPE html>
<html lang="en">
<head>
<meta charset="utf-8">
<title>Varnoli – Business Card</title>
<link rel="stylesheet" href="https://fonts.googleapis.com/css2?family=Open+Sans:wght@400;600;700&display=swap">
<style>
  :root {
    --brand-green: #77c41d;
    --ink: #2b2b2b;
    --muted-grey: #707173;
    --card-white: #ffffff;
    --backdrop: #e9e7e3;
  }
  * { box-sizing: border-box; margin: 0; padding: 0; }
  html, body {
    width: 1200px;
    height: 900px;
    overflow: hidden;
    background: var(--backdrop);
    font-family: "Open Sans", Arial, sans-serif;
  }
  .canvas {
    position: relative;
    width: 1200px;
    height: 900px;
  }
  .card {
    position: absolute;
    left: 290px;
    width: 620px;
    height: 354px;
    background: var(--card-white);
    box-shadow: 0 2px 10px rgba(0,0,0,0.12);
  }
  .card--front { top: 64px; }
  .card--back { top: 482px; }

  /* Brand lockup */
  .brand {
    position: absolute;
    display: flex;
    flex-direction: column;
    align-items: flex-start;
  }
  .card--front .brand {
    left: 50%;
    top: 50%;
    transform: translate(-50%, -50%);
  }
  .brand__row {
    display: flex;
    align-items: center;
    gap: 10px;
  }
  .brand__dot {
    width: 14px;
    height: 14px;
    border-radius: 50%;
    background: var(--brand-green);
  }
  .brand__name {
    color: var(--brand-green);
    font-weight: 700;
    font-size: 54px;
    line-height: 1;
    letter-spacing: 1px;
  }
  .brand__tagline {
    color: var(--muted-grey);
    font-weight: 600;
    font-size: 14px;
    letter-spacing: 1.6px;
    margin-top: 8px;
  }

  /* Back */
  .card--back .brand {
    left: 40px;
    top: 34px;
  }
  .card--back .brand__name { font-size: 28px; letter-spacing: 0.5px; }
  .card--back .brand__dot { width: 8px; height: 8px; }
  .card--back .brand__row { gap: 6px; }
  .card--back .brand__tagline { font-size: 7.5px; letter-spacing: 0.9px; margin-top: 4px; }

  .person {
    position: absolute;
    left: 40px;
    top: 108px;
  }
  .person__name {
    color: var(--brand-green);
    font-weight: 600;
    font-size: 15px;
  }
  .person__title {
    color: var(--ink);
    font-size: 14px;
  }
  .address {
    position: absolute;
    left: 40px;
    top: 168px;
    display: flex;
    gap: 6px;
    color: var(--ink);
    font-size: 12.5px;
    line-height: 1.45;
  }
  .contact-list {
    position: absolute;
    right: 56px;
    bottom: 44px;
    list-style: none;
    display: flex;
    flex-direction: column;
    gap: 10px;
  }
  .contact-list__item {
    display: flex;
    align-items: center;
    gap: 12px;
    color: var(--ink);
    font-size: 16px;
    letter-spacing: 0.3px;
  }
  .contact-list__item--web { color: var(--brand-green); }
  .contact-list__item--phone { margin-bottom: 26px; }
  .icon { width: 13px; height: 13px; flex: none; fill: var(--brand-green); }
  .address .icon { margin-top: 3px; }
</style>
</head>
<body>
<main class="canvas">

  <section class="card card--front" aria-label="Business card front">
    <div class="brand">
      <div class="brand__row">
        <span class="brand__dot"></span>
        <span class="brand__name">VARNOLI</span>
      </div>
      <span class="brand__tagline">IT SOLUTIONS FOR SMALL BUSINESS</span>
    </div>
  </section>

  <section class="card card--back" aria-label="Business card back">
    <div class="brand">
      <div class="brand__row">
        <span class="brand__dot"></span>
        <span class="brand__name">VARNOLI</span>
      </div>
      <span class="brand__tagline">IT SOLUTIONS FOR SMALL BUSINESS</span>
    </div>

    <div class="person">
      <p class="person__name">Dana Whitlow</p>
      <p class="person__title">Director</p>
    </div>

    <div class="address">
      <svg class="icon" viewBox="0 0 12 16" aria-hidden="true">
        <path d="M6 0C2.7 0 0 2.6 0 5.9 0 10 6 16 6 16s6-6 6-10.1C12 2.6 9.3 0 6 0zm0 8.2a2.3 2.3 0 1 1 0-4.6 2.3 2.3 0 0 1 0 4.6z"/>
      </svg>
      <p>27 Fernbrook Road<br>Marlow QLD 4000</p>
    </div>

    <ul class="contact-list">
      <li class="contact-list__item contact-list__item--phone">
        <svg class="icon" viewBox="0 0 16 16" aria-hidden="true">
          <path d="M3.6 1.2 5.7 3.4c.4.4.4 1 0 1.4L4.6 5.9c.9 2 2.9 4 5 5l1.1-1.1c.4-.4 1-.4 1.4 0l2.2 2.1c.4.4.4 1 0 1.4l-1.2 1.2c-.8.8-2 1-3 .6C6 13.4 2.6 10 1 5.9.6 4.9.8 3.7 1.6 2.9l.6-.6c.4-.4 1-.4 1.4-.1z"/>
        </svg>
        <span>+61 400 000 000</span>
      </li>
      <li class="contact-list__item">
        <svg class="icon" viewBox="0 0 16 12" aria-hidden="true">
          <path d="M0 0h16v1.2L8 6.5 0 1.2zM0 2.8l8 5.3 8-5.3V12H0z"/>
        </svg>
        <span>hello@varnoli.com</span>
      </li>
      <li class="contact-list__item contact-list__item--web">
        <svg class="icon" viewBox="0 0 16 16" aria-hidden="true">
          <circle cx="8" cy="8" r="7.5"/>
          <path d="M1 8h14M8 .5c2.5 2.6 2.5 12.4 0 15M8 .5c-2.5 2.6-2.5 12.4 0 15" stroke="#fff" stroke-width="1" fill="none"/>
        </svg>
        <span>www.varnoli.com</span>
      </li>
    </ul>
  </section>

</main>
</body>
</html>
```